GHollis Busisness Card

I am an aerospace consultant and at this time only need business cards.

Industry/Entity Type

Business

Contact Information for Business Card

Hollis Partners,LLC
Gerald T. Hollis

348 Birch Hollow Road
Madison AL 35762

256-555-0148 (cell)
256-555-0173 (fax)

geraldhollis@mailbrook.net

```html
<!DOCTYPE html>
<html lang="en">
<head>
<meta charset="utf-8">
<title>Hollis Partners, LLC — Business Card</title>
<link rel="stylesheet" href="https://fonts.googleapis.com/css2?family=Open+Sans:wght@400;700&display=swap">
<style>
  :root {
    --page-bg: #f6f7f7;
    --card-bg: #38383a;
    --band-blue: #0e5c99;
    --band-edge: #1e2a38;
    --ink-light: #ffffff;
    --card-shadow: rgba(0, 0, 0, 0.35);
  }
  * { margin: 0; padding: 0; box-sizing: border-box; }
  html, body {
    width: 1200px;
    height: 999px;
    overflow: hidden;
    background: var(--page-bg);
    font-family: "Open Sans", Arial, sans-serif;
  }
  .business-card {
    position: absolute;
    left: 75px;
    top: 199px;
    width: 1050px;
    height: 600px;
    background: var(--card-bg);
    box-shadow: 4px 6px 8px var(--card-shadow);
  }
  .info-band {
    position: absolute;
    left: 0;
    width: 447px;
    background: var(--band-blue);
    box-shadow: 3px 3px 0 var(--band-edge);
    color: var(--ink-light);
  }
  .info-band--identity {
    top: 165px;
    height: 135px;
    padding: 16px 0 0 42px;
    font-size: 25px;
    line-height: 35px;
  }
  .identity-name { font-weight: 700; }
  .info-band--contact {
    top: 340px;
    height: 136px;
    padding: 8px 0 0 36px;
  }
  .contact-row {
    display: flex;
    align-items: center;
    height: 41.5px;
    font-size: 25px;
  }
  .contact-icon {
    width: 32px;
    height: 32px;
    margin-right: 12px;
    flex: none;
  }
  .brand-name {
    position: absolute;
    left: 538px;
    top: 198px;
    width: 450px;
    text-align: center;
    color: var(--ink-light);
    font-weight: 700;
    text-transform: uppercase;
  }
  .brand-name__main {
    display: block;
    font-size: 100px;
    line-height: 120px;
    letter-spacing: 1px;
  }
  .brand-name__sub {
    display: block;
    font-size: 40px;
    line-height: 52px;
  }
</style>
</head>
<body>
  <main class="business-card">
    <section class="info-band info-band--identity">
      <p class="identity-name">Gerald T.</p>
      <p>Hollis 348 Birch Hollow</p>
      <p>Road Madison AL</p>
    </section>

    <section class="info-band info-band--contact">
      <p class="contact-row">
        <svg class="contact-icon" viewBox="0 0 32 32" aria-hidden="true">
          <rect x="2" y="1" width="28" height="30" rx="5" fill="#fff"/>
          <path d="M11 6c-2 1-3 3-2 7 1 5 4 10 8 13 2 1 4 1 5-1l-3-4-2 1c-2-2-3-4-4-7l2-1-1-6z" fill="#0e5c99"/>
        </svg>
        <span>35762 256-555-0148</span>
      </p>
      <p class="contact-row">
        <svg class="contact-icon" viewBox="0 0 32 32" aria-hidden="true">
          <rect x="9" y="1" width="14" height="12" fill="#fff"/>
          <rect x="11" y="4" width="10" height="1.5" fill="#0e5c99"/>
          <rect x="11" y="7" width="10" height="1.5" fill="#0e5c99"/>
          <rect x="3" y="14" width="26" height="17" rx="3" fill="#fff"/>
          <path d="M8 24c3-4 13-4 16 0l-3 2-2-2h-6l-2 2z" fill="#0e5c99"/>
        </svg>
        <span>256-555-0173</span>
      </p>
      <p class="contact-row">
        <svg class="contact-icon" viewBox="0 0 32 32" aria-hidden="true">
          <path d="M2 13L16 3l14 10v16H2z" fill="#fff"/>
          <path d="M4 14l12 9 12-9" fill="none" stroke="#0e5c99" stroke-width="2"/>
          <path d="M13 12h6v-3h-6zM10 12l6 6 6-6z" fill="#0e5c99"/>
        </svg>
        <span>geraldhollis@mailbrook.net</span>
      </p>
    </section>

    <h1 class="brand-name">
      <span class="brand-name__main">Hollis</span>
      <span class="brand-name__sub">Partners, LLC</span>
    </h1>
  </main>
</body>
</html>
```